*YO!!! Designers Needed!!* Front Page Cover Needed for a $$Billion Dollar$$ Company

We are a manufacturer of aluminum electrolytic capacitors. We are looking to create a front page cover that will be used on our annual report. We are a publicly listed company and work with many Pinnacle 300 companies, so your work will be viewed by the BIG GUNS and EXECUTIVES around the WORLD! If selected, you may be selected for additional work.

The front page cover should be unique. If elegance, modern, bling, and creativity somehow got together and had a child, that's what the cover page would look like!

Inspired Examples attached. Check them out!

www.velmoro.com

Font styles to use
Sans Serif

Requirements
Must have
• 1. Must include the attached logo. Logo size, color, and placement are at your discretion.

2. Should include the text, '2020 Annual Report'

3. The design should incorporate the use of foil and/or be embossed. The foil can be part of the design or can be the full page. See various examples attached for reference.

4. Shall be in A4 size and vertical orientation.
Nice to have
• Feel free to add any icons or stock photos (for example capacitors or circuit boards) if needed.

Be creative here and don't be afraid to be bold! The end product will be printed and budget is not a limiting factor, so feel free to make it extravagant if needed.

Our slogan is "Think Ahead". This slogan can or cannot be part of the theme.

```html
<!DOCTYPE html>
<html lang="en">
<head>
<meta charset="utf-8">
<title>Velmoro 2020 Annual Report Cover</title>
<link href="https://fonts.googleapis.com/css2?family=Montserrat:wght@200;400;600;800&display=swap" rel="stylesheet">
<style>
  :root {
    --paper-top: #ffffff;
    --paper-bottom: #ebe8e5;
    --teal-deep: #257e92;
    --teal-light: #86bfb6;
    --slate-blue: #336a86;
    --white: #ffffff;
  }
  html, body {
    margin: 0;
    padding: 0;
    overflow: hidden;
  }
  .cover {
    position: relative;
    width: 848px;
    height: 1200px;
    overflow: hidden;
    background: linear-gradient(180deg, var(--paper-top), var(--paper-bottom));
    font-family: "Montserrat", sans-serif;
    color: var(--white);
  }
  .cover-art {
    position: absolute;
    inset: 0;
  }
  .title-frame {
    position: absolute;
    left: 0;
    top: 0;
  }
  .title-year {
    position: absolute;
    left: 526px;
    top: 215px;
    font-weight: 200;
    font-size: 62px;
    line-height: 1;
    letter-spacing: -1px;
  }
  .title-main {
    position: absolute;
    left: 526px;
    top: 283px;
    font-weight: 800;
    font-size: 61px;
    line-height: 67px;
    letter-spacing: 0;
  }
  .brand {
    position: absolute;
    left: 117px;
    top: 800px;
    width: 320px;
    text-align: right;
  }
  .brand-name {
    display: block;
    font-weight: 600;
    font-size: 62px;
    line-height: 1;
    letter-spacing: 1px;
  }
  .brand-slogan {
    display: block;
    margin-top: 40px;
    font-weight: 400;
    font-size: 21px;
    letter-spacing: 1.5px;
  }
  .dot-grid {
    position: absolute;
    left: 741px;
    top: 1083px;
  }
</style>
</head>
<body>
<main class="cover">
  <svg class="cover-art" width="848" height="1200" viewBox="0 0 848 1200" xmlns="http://www.w3.org/2000/svg">
    <defs>
      <linearGradient id="teal-sweep" x1="0" y1="1" x2="1" y2="0">
        <stop offset="0" stop-color="var(--teal-deep)"/>
        <stop offset="1" stop-color="var(--teal-light)"/>
      </linearGradient>
    </defs>
    <path class="circuit-field" role="img" aria-label="Circuit board trace pattern in teal"
          d="M0,313 C300,300 520,150 524,0 L848,0 L848,495 C650,475 400,485 240,545 C100,600 20,700 0,779 Z"
          fill="url(#teal-sweep)"/>
    <path class="facet-panel facet-panel--top" role="img" aria-label="Low-poly faceted blue surface"
          d="M85,0 L464,0 C450,140 300,240 85,246 Z" fill="var(--slate-blue)"/>
    <path class="facet-panel facet-panel--bottom" role="img" aria-label="Low-poly faceted blue surface"
          d="M464,556 L464,1200 L85,1200 L85,815 C90,650 250,565 464,556 Z" fill="var(--slate-blue)"/>
  </svg>

  <svg class="title-frame" width="848" height="1200" viewBox="0 0 848 1200" fill="none" stroke="var(--white)">
    <path d="M462,263 L462,196 L806,196 L806,451 L462,451 L462,385" stroke-width="3"/>
    <g class="report-icon" stroke-width="1.6" stroke-linecap="round" stroke-linejoin="round">
      <path d="M501,293 L501,282 L438,282 L438,344"/>
      <path d="M438,350 L438,368 L501,368 L501,298"/>
      <rect x="455" y="288" width="29" height="6"/>
      <circle cx="452" cy="308" r="8"/>
      <path d="M452,300 L452,308 L460,308"/>
      <path d="M469,299 H495 M469,305 H495 M469,311 H495 M469,317 H486"/>
      <path d="M445,326 H470 M445,332 H470 M445,338 H458"/>
      <rect x="444" y="357" width="8" height="5"/>
      <rect x="458" y="349" width="8" height="13"/>
      <rect x="472" y="339" width="8" height="23"/>
      <path d="M486,362 V331 H494 V336 M494,342 V362 H486"/>
    </g>
  </svg>

  <div class="title-year">2020</div>
  <h1 class="title-main" style="margin:0">Annual<br>Report</h1>

  <div class="brand">
    <span class="brand-name">VELMORO</span>
    <span class="brand-slogan">THINK AHEAD.</span>
  </div>

  <svg class="dot-grid" width="84" height="88" viewBox="0 0 84 88" fill="var(--white)">
    <circle cx="9" cy="9" r="9"/><circle cx="41" cy="9" r="9"/><circle cx="74" cy="9" r="9"/>
    <circle cx="9" cy="44" r="9"/><circle cx="41" cy="44" r="9"/><circle cx="74" cy="44" r="9"/>
    <circle cx="9" cy="79" r="9"/><circle cx="41" cy="79" r="9"/><circle cx="74" cy="79" r="9"/>
  </svg>
</main>
</body>
</html>
```